Letter head / email signature/ contract document templates

We need a professional email signature and letterhead designed for our established carpentry and maintenance company. Our Logo (attached) was originally designed 6 years ago by design guru and we love it, looking for something to compliment it ( not a home job)

```html
<!DOCTYPE html>
<html lang="en">
<head>
<meta charset="utf-8">
<title>Harbourline Handyworks – Stationery</title>
<link href="https://fonts.googleapis.com/css2?family=Montserrat:wght@400;700&family=Arimo:wght@400;700&display=swap" rel="stylesheet">
<style>
:root{
  --stage:#ababab;
  --paper:#f6f6f7;
  --red:#f00000;
  --ink:#333436;
  --muted:#8a8a8a;
  --rule:#8c8c8c;
}
*{box-sizing:border-box;margin:0;padding:0}
html,body{width:1063px;height:1200px;overflow:hidden}
body{background:var(--stage);position:relative;font-family:"Montserrat",sans-serif;color:var(--ink)}
.sheet{position:absolute;box-shadow:1px 2px 3px rgba(0,0,0,.35);overflow:hidden}

/* brand mark */
.brand{display:flex;align-items:center;gap:5px;font-family:"Montserrat",sans-serif;font-weight:700;color:var(--ink);white-space:nowrap}
.brand .dot{background:var(--red);flex:none}

/* letterhead */
.letterhead{left:46px;top:89px;width:474px;height:670px;background:linear-gradient(180deg,#f4f4f5,#fafafa 60%,#f1f1f2)}
.letterhead .brand{position:absolute;left:31px;top:34px;font-size:15px}
.letterhead .brand .dot{width:10px;height:10px}
.contact-block{position:absolute;font-family:"Arimo",sans-serif;color:var(--ink)}
.letterhead .contact-block{left:353px;top:21px;font-size:7.3px;line-height:9.6px}
.contact-block .row{display:flex;align-items:center;gap:4px}
.contact-block .gap{margin-top:5px}
.contact-block svg{width:6px;height:6px;flex:none}
.letterhead .head-rule{position:absolute;left:31px;top:82px;width:411px;height:1px;background:var(--rule)}
.recipient{position:absolute;left:63px;top:150px;font-size:5.6px;line-height:10.5px;color:var(--muted)}
.recipient .to{font-size:8px;color:var(--ink);letter-spacing:1px}
.recipient .name{font-size:7.5px;color:var(--red)}
.date{position:absolute;right:32px;top:150px;font-size:5.8px;color:var(--muted)}
.body-copy{position:absolute;left:63px;top:239px;width:379px;font-size:6.1px;line-height:8.5px;color:#9a9a9a;text-align:justify}
.body-copy p{margin-bottom:8.3px}
.signature{position:absolute;left:63px;top:472px;width:85px;height:18px;background:linear-gradient(90deg,#e6e6e8,#f3f3f4)}
.signer{position:absolute;left:63px;top:497px;font-size:7.8px;line-height:10px}
.signer small{display:block;font-size:5.6px;color:var(--muted)}

/* folder closed */
.folder{left:553px;width:454px;height:321px}
.folder-closed{top:89px;background:linear-gradient(100deg,#cfcfd1 50%,#f3f3f4 68%,#fff 85%)}
.folder-closed .cover{position:absolute;left:0;top:0;width:227px;height:100%;background:var(--red)}
.folder-closed .brand{position:absolute;right:16px;top:26px;font-size:9px;gap:3px}
.folder-closed .brand .dot{width:6px;height:6px}
.mini-contact{position:absolute;right:24px;top:298px;display:flex;gap:4px;font-family:"Arimo",sans-serif;font-size:3.2px;line-height:4.4px;color:var(--ink)}
.mini-contact .addr{text-align:right;border-right:0.5px solid var(--rule);padding-right:4px}
.mini-contact .dot{display:inline-block;width:2.4px;height:2.4px;border-radius:50%;background:var(--red);margin-right:2px}

/* folder open */
.folder-open{top:438px;background:linear-gradient(90deg,#fafafa,#e5e5e7 45%,#cdcdcf 50%,#e5e5e7 55%,#fafafa)}
.mini-letter{position:absolute;left:238px;top:16px;width:205px;height:250px;background:#f5f5f6;padding:11px 14px}
.mini-letter .brand{font-size:7px;gap:2px}
.mini-letter .brand .dot{width:4.5px;height:4.5px}
.mini-letter .mini-head{position:absolute;right:14px;top:10px;font-family:"Arimo",sans-serif;font-size:2.6px;line-height:3.4px}
.mini-letter .mini-rule{position:absolute;left:14px;right:14px;top:35px;height:0.5px;background:var(--rule)}
.mini-letter .mini-to{position:absolute;left:27px;top:64px;font-size:2.5px;line-height:4px;color:var(--muted)}
.mini-letter .mini-to b{color:var(--red);font-weight:400}
.mini-letter .mini-date{position:absolute;right:14px;top:64px;font-size:2.3px;color:var(--muted)}
.mini-letter .mini-copy{position:absolute;left:27px;right:14px;top:104px;font-size:2.5px;line-height:3.6px;color:#a3a3a3;text-align:justify}
.mini-letter .mini-copy p{margin-bottom:3.5px}
.pockets{position:absolute;left:0;top:0;width:454px;height:321px}

/* email signature */
.email-signature{left:46px;top:816px;width:960px;height:296px;background:linear-gradient(90deg,#f1f1f2,#fafafa 55%,#f3f3f4)}
.email-signature .brand{position:absolute;left:60px;top:78px;width:340px;font-size:40px;line-height:46px;gap:14px;align-items:flex-end;white-space:normal}
.email-signature .brand .dot{width:24px;height:24px;margin-bottom:10px}
.divider{position:absolute;left:425px;top:42px;width:2px;height:170px;background:#333}
.person{position:absolute;left:460px;top:42px;font-family:"Arimo",sans-serif}
.person .name{font-size:29px;font-weight:700;color:var(--red);line-height:34px}
.person .role{font-size:23px;color:var(--ink);line-height:28px}
.person .lines{margin-top:18px}
.person .line{display:flex;align-items:center;gap:14px;font-size:24.5px;line-height:30px;color:var(--ink)}
.person .line svg{width:20px;height:20px;flex:none}
.sig-rule{position:absolute;left:50px;top:228px;width:861px;height:2px;background:#333}
.sig-address{position:absolute;left:0;width:100%;top:241px;text-align:center;font-family:"Arimo",sans-serif;font-size:24px;color:var(--ink)}
</style>
</head>
<body>

<svg width="0" height="0" style="position:absolute" aria-hidden="true">
  <defs>
    <symbol id="i-phone" viewBox="0 0 24 24"><path fill="#f00000" d="M6.6 10.8a15.1 15.1 0 0 0 6.6 6.6l2.2-2.2a1 1 0 0 1 1-.25 11.4 11.4 0 0 0 3.6.57 1 1 0 0 1 1 1V20a1 1 0 0 1-1 1A17 17 0 0 1 3 4a1 1 0 0 1 1-1h3.5a1 1 0 0 1 1 1c0 1.25.2 2.45.57 3.57a1 1 0 0 1-.25 1z"/></symbol>
    <symbol id="i-mail" viewBox="0 0 24 24"><rect x="2" y="5" width="20" height="14" fill="#f00000"/><path d="M2 5l10 8 10-8M2 19l8-7M22 19l-8-7" fill="none" stroke="#fff" stroke-width="1.6"/></symbol>
    <symbol id="i-web" viewBox="0 0 24 24"><circle cx="12" cy="12" r="10" fill="#f00000"/><path d="M2 12h20M12 2c3 3 3 17 0 20M12 2c-3 3-3 17 0 20" fill="none" stroke="#fff" stroke-width="1.5"/></symbol>
  </defs>
</svg>

<!-- Letterhead -->
<section class="sheet letterhead">
  <div class="brand"><span>Harbourline Handyworks</span><span class="dot"></span></div>
  <div class="contact-block">
    <div>Your address, city</div>
    <div>state, ZIP 0000</div>
    <div class="row gap"><svg><use href="#i-phone"/></svg>123-456-2100</div>
    <div class="row"><svg><use href="#i-mail"/></svg>youremail@gmail.com</div>
    <div class="row"><svg><use href="#i-web"/></svg>www.yourwebsite.com</div>
  </div>
  <div class="head-rule"></div>

  <div class="recipient">
    <div class="to">TO</div>
    <div class="name">Dana Whitcombe</div>
    <div>Human Resources</div>
    <div>Brightfield Ltd.</div>
    <div>42 Elm Row, Fairmont</div>
    <div>F27 USA</div>
  </div>
  <div class="date">Friday, 01/01/2018</div>

  <div class="body-copy">
    <p>Lorem ipsum dolor sit amet, consectetuer adipiscing elit, sed diam nonummy nibh euismod tincidunt ut laoreet dolore magna aliquam erat volutpat. Ut wisi enim ad minim veniam, quis nostrud exerci tationmcorper suscipit lobortis nisl ut aliquip ex ea commodo consequat. Duis autem vel eum iriure dolor in hendrerit in vulputate velit esse molestie consequat, vel illum dolore eu feugiat nulla facilisis at vero eros et accumsan et iusto odio dignissim qui blandit praesent luptatum zzril delenit augue duis dolore te feugait nulla facilisi.</p>
    <p>Nam liber tempor cum soluta nobis eleifend option congue nihil imprdiet doming id quod mazim placerat facer possim assum. Typi non habent claritatem insitam;</p>
    <p>Est usus legentis in iis qui facit eorum claritatem.</p>
    <p>Investigationes demonstraverunt lectores legere me lius quod ii legunt saepius. Claritas est etiam processus dynamicus, qui sequitur mutationem consuetudium lectorum. Mirum est notare quam littera gothica, quam nunc putamus parum claram, anteposuerit litterarum formas humanitatis per seacula quarta decima et quinta decima. Eodem modo typi, qui nunc nobis videntur parum clari, fiant sollemnes in futurum.</p>
    <p>consectetuer adipiscing elit, sed diam nonummy nibh euismod tincidunt ut laoreet dolore magna aliquam erat volutpat. Ut wisi enim ad minim veniam, quis nostrud exerci tation ullamcorper suscipit lobortis nisl ut aliquip ex ea commodo consequat. Duis autem vel eum iriure dolor in hendrerit in vulputate velit esse molestie consequat, vel illum dolore eu feugiat nulla facilisis at vero eros et accumsan et iusto odio dignissim qui blandit praesent luptatum zzril delenit augue duis dolore te feugait nulla facilisi.</p>
    <p>Nam liber tempor cum soluta nobis eleifend option congue nihil imperdiet .</p>
  </div>

  <div class="signature" role="img" aria-label="Handwritten signature of Owen Hartley"></div>
  <div class="signer">Owen Hartley<small>Managing Director</small></div>
</section>

<!-- Folder, closed -->
<section class="sheet folder folder-closed">
  <div class="cover"></div>
  <div class="brand"><span>Harbourline Handyworks</span><span class="dot"></span></div>
  <div class="mini-contact">
    <div class="addr">Your address, city<br>state, ZIP 0000</div>
    <div><span class="dot"></span>123-456-2100<br><span class="dot"></span>youremail@gmail.com<br><span class="dot"></span>www.yourwebsite.com</div>
  </div>
</section>

<!-- Folder, open -->
<section class="sheet folder folder-open">
  <div class="mini-letter">
    <div class="brand"><span>Harbourline Handyworks</span><span class="dot"></span></div>
    <div class="mini-head">Your address, city<br>state, ZIP 0000<br>123-456-2100<br>youremail@gmail.com<br>www.yourwebsite.com</div>
    <div class="mini-rule"></div>
    <div class="mini-to">TO<br><b>Dana Whitcombe</b><br>Human Resources<br>Brightfield Ltd.<br>42 Elm Row, Fairmont<br>F27 USA</div>
    <div class="mini-date">Friday, 01/01/2018</div>
    <div class="mini-copy">
      <p>Lorem ipsum dolor sit amet, consectetuer adipiscing elit, sed diam nonummy nibh euismod tincidunt ut laoreet dolore magna.</p>
      <p>Nam liber tempor cum soluta nobis eleifend option congue nihil.</p>
      <p>Est usus legentis in iis qui facit eorum claritatem.</p>
      <p>Investigationes demonstraverunt lectores legere me lius quod ii legunt saepius.</p>
      <p>Nam liber tempor cum soluta nobis eleifend.</p>
    </div>
  </div>
  <svg class="pockets" viewBox="0 0 454 321" aria-hidden="true">
    <path fill="var(--red)" d="M0 207H199Q209 207 211 220L227 321H0Z"/>
    <path fill="var(--red)" d="M454 207H250Q240 207 238 220L227 321H454Z"/>
  </svg>
</section>

<!-- Email signature -->
<section class="sheet email-signature">
  <div class="brand"><span>Harbourline<br>Handyworks</span><span class="dot"></span></div>
  <div class="divider"></div>
  <div class="person">
    <div class="name">Marcus Bell</div>
    <div class="role">Manager</div>
    <div class="lines">
      <div class="line"><svg><use href="#i-phone"/></svg>123-456-2100</div>
      <div class="line"><svg><use href="#i-mail"/></svg>youremail@gmail.com</div>
      <div class="line"><svg><use href="#i-web"/></svg>www.yourwebsite.com</div>
    </div>
  </div>
  <div class="sig-rule"></div>
  <div class="sig-address">Your address, city, state, ZIP 0000</div>
</section>

</body>
</html>
```